Restaurant Website

I want to build a website for my restaurant. we specialise in Handmade Noodles and various stir fries. The cuisine is Asian Fusion.
Main colours of the website should be Red, White and Black.

I will have the logo attached, as well as. the menu.

The website should have 4 pages:

Main page
Menu page (menu should have photos)
Our story
Contact us

```html
<!DOCTYPE html>
<html lang="en">
<head>
<meta charset="utf-8">
<title>KORAM – Handmade Noodles</title>
<link href="https://fonts.googleapis.com/css2?family=Lora:wght@600;700&family=Roboto:wght@400;500;700&display=swap" rel="stylesheet">
<style>
:root{--red:#a81c24;--red-dark:#8e1219;--black:#000;--white:#fff;--ink:#1a1a1a;--grey:#4a4a4a;--pink:#f3e1e1;}
*{box-sizing:border-box;margin:0;padding:0}
html,body{width:1200px;height:3338px;overflow:hidden;background:var(--white);font-family:'Roboto',sans-serif;color:var(--ink)}
.page{position:relative;width:1200px;height:3338px}
.abs{position:absolute}
.header{left:0;top:0;width:1200px;height:145px;background:var(--black)}
.nav a{position:absolute;top:57px;height:31px;line-height:31px;color:var(--white);font-size:13px;font-weight:700;text-decoration:none;padding:0 19px;border-radius:16px}
.nav a.active{background:var(--red)}
.brand{position:absolute;display:flex;align-items:center;gap:8px;color:var(--white);font-family:'Lora',serif;font-weight:700;font-size:22px;letter-spacing:2px}
.brand i{display:block;width:18px;height:18px;border-radius:50%;background:var(--red)}
.btn-outline{position:absolute;left:761px;top:49px;width:176px;height:47px;border:2px solid var(--white);border-radius:24px;color:var(--white);font-size:14px;font-weight:700;text-align:center;line-height:43px}
.social{position:absolute;width:36px;height:36px;border-radius:50%;background:var(--white);display:flex;align-items:center;justify-content:center}
.social::after{content:"";width:12px;height:12px;border-radius:50%;background:var(--black)}
.social.red{background:var(--red)}
.social.red::after{background:var(--white)}
.hero-photo{left:0;top:145px;width:1200px;height:704px;background:radial-gradient(ellipse at 55% 55%,#a88a64 0%,#6b4e34 40%,#2d2119 80%)}
.hero-curve{left:0;top:145px}
.hero-title{left:0;top:370px;width:1200px;text-align:center;color:var(--white);font-family:'Lora',serif;font-weight:700;font-size:58px}
.hero-sub{left:290px;top:446px;width:620px;text-align:center;color:var(--white);font-size:20px;line-height:31px}
.btn-red{position:absolute;background:var(--red);color:var(--white);font-weight:700;font-size:15px;text-align:center;border-radius:25px}
.dot{position:absolute;top:781px;width:8px;height:8px;border-radius:50%;background:var(--white)}
.circle{position:absolute;border-radius:50%}
.section-title{font-family:'Lora',serif;font-weight:700;font-size:40px;color:var(--ink)}
.story-title{left:648px;top:950px;border-left:4px solid var(--red);padding-left:18px;line-height:40px}
.story-text{left:648px;width:442px;font-size:14.5px;line-height:26.5px;color:var(--grey)}
.menus{left:0;top:1454px;width:1200px;height:639px;background:radial-gradient(ellipse at 50% 40%,#b12129,#9c1820 70%,#8e1219)}
.center-title{left:0;width:1200px;text-align:center}
.underline{position:absolute;left:560px;width:80px;height:4px;background:var(--red)}
.tab{position:absolute;height:45px;line-height:41px;border:2px solid var(--white);border-radius:23px;color:var(--white);font-size:14px;font-weight:700;text-align:center}
.tab.active{background:var(--white);color:var(--ink)}
.dish{position:absolute;top:1764px;width:220px}
.dish .photo{position:absolute;left:0;top:0;width:220px;height:220px;border-radius:50%;border:6px solid var(--white)}
.dish .card{position:absolute;left:8px;top:176px;width:204px;height:71px;background:var(--white);border-radius:6px;text-align:center;padding-top:14px}
.dish .name{font-size:14px;font-weight:500;color:var(--ink)}
.dish .price{font-size:14px;font-weight:700;color:var(--red);margin-top:6px}
.arrow{position:absolute;top:1855px;width:36px;height:36px;border-radius:50%;background:var(--white)}
.tile{position:absolute;border-radius:4px}
.footer-col{position:absolute;top:3050px;color:var(--white)}
.footer-col h4{font-size:18px;font-weight:500;margin-bottom:16px;letter-spacing:.2px}
.link{display:flex;align-items:center;gap:18px;font-size:14px;height:43px}
.info{display:flex;gap:18px;margin-bottom:14px}
.info b{display:block;font-size:14px;font-weight:700;margin-bottom:4px}
.info span{font-size:11.5px;line-height:18px}
.newsletter{width:315px;height:42px;background:var(--white);border-radius:21px;color:var(--ink);font-size:13px;padding:0 18px;display:flex;align-items:center;justify-content:space-between}
.rule{left:111px;top:3288px;width:978px;height:1px;background:#444}
.copy{left:0;top:3306px;width:1200px;text-align:center;color:var(--white);font-size:12px}
</style>
</head>
<body>
<div class="page">

<header class="abs header">
  <nav class="nav">
    <a class="active" style="left:91px">HOME</a>
    <a style="left:166px">MENU</a>
    <a style="left:241px">OUR STORY</a>
    <a style="left:349px">CONTACT US</a>
  </nav>
  <div class="brand" style="left:538px;top:57px"><i></i>KORAM</div>
  <div class="btn-outline">MAKE A BOOKING</div>
  <span class="social red" style="left:967px;top:55px"></span>
  <span class="social" style="left:1010px;top:55px"></span>
  <span class="social" style="left:1052px;top:55px"></span>
</header>

<div class="abs hero-photo" role="img" aria-label="Chef pulling fresh handmade noodles on a floured wooden table"></div>
<svg class="abs hero-curve" width="1200" height="704" viewBox="0 0 1200 704">
  <path d="M0,548 Q600,924 1200,345 L1200,704 L0,704 Z" fill="#a81c24"/>
  <path d="M0,555 Q600,940 1200,385 L1200,704 L0,704 Z" fill="#fff"/>
</svg>
<h1 class="abs hero-title">WELCOME TO KORAM</h1>
<p class="abs hero-sub">Lorem ipsum dolor sit amet, consectetur adipiscing elit, sed do eiusmod tempor incididunt ut laborea.</p>
<div class="btn-red" style="left:512px;top:528px;width:176px;height:47px;line-height:47px">VIEW OUR MENUS</div>
<span class="dot" style="left:556px"></span>
<span class="abs" style="left:577px;top:775px;width:20px;height:20px;border:2px solid #fff;border-radius:50%"></span>
<span class="dot" style="left:583px;top:781px"></span>
<span class="dot" style="left:609px"></span>
<span class="dot" style="left:636px"></span>

<section>
  <span class="circle" style="left:214px;top:1153px;width:208px;height:208px;background:var(--pink)"></span>
  <span class="circle" role="img" aria-label="Bowl of tomato noodle soup on rustic wood" style="left:111px;top:917px;width:340px;height:340px;background:radial-gradient(circle,#c0542f 0%,#8d7b68 45%,#5a524a 100%)"></span>
  <span class="circle" role="img" aria-label="Bowl of braised beef stew" style="left:373px;top:972px;width:156px;height:156px;border:6px solid #fff;background:radial-gradient(circle,#7a3a1c,#3f3330 70%,#8aa0a8)"></span>
  <span class="circle" role="img" aria-label="Plate of pilaf rice topped with lamb" style="left:309px;top:1080px;width:290px;height:290px;border:6px solid #fff;background:radial-gradient(circle,#d9a27a 0%,#c88a63 45%,#3a3a3c 75%,#9b9b9b)"></span>

  <h2 class="abs section-title story-title">OUR STORY</h2>
  <p class="abs story-text" style="top:1020px">Lorem ipsum dolor sit amet, consectetur adipiscing elit, sed do eiusmod tempor incididunt ut labore et dolore magna aliqua. Ut enim ad minim veniam, quis nostrud exercitation ullamco laboris nisi ut aliquip ex ea commodo consequat. Duis aute irure dolor in reprehenderit in voluptate velit essea.</p>
  <p class="abs story-text" style="top:1165px">Lorem ipsum dolor sit amet, consectetur adipiscing elit, sed do eiusmod tempor incididunt ut labore et dolore magna aliqua. Ut enim ad minim veniam, quisea.</p>
  <div class="btn-red" style="left:648px;top:1280px;width:149px;height:47px;line-height:47px">LEARN MORE</div>
  <div class="abs" role="img" aria-label="Whole roast lamb on a wooden board with teapot and grapes" style="left:868px;top:1240px;width:332px;height:214px;background:radial-gradient(ellipse at 50% 60%,#a8662a 0%,#6e3d1c 45%,rgba(255,255,255,0) 72%)"></div>
</section>

<section class="abs menus" role="img" aria-label="Red tinted background of spices and kitchen tools">
</section>
<h2 class="abs section-title center-title" style="top:1522px;color:#fff">OUR MENUS</h2>
<span class="underline" style="top:1576px;background:#fff"></span>
<div class="tab" style="left:141px;top:1619px;width:127px">ENTRÉES</div>
<div class="tab active" style="left:277px;top:1619px;width:264px">HOMEMADE NOODLES &amp; BUNS</div>
<div class="tab" style="left:550px;top:1619px;width:177px">HOUSE SPECIALS</div>
<div class="tab" style="left:736px;top:1619px;width:144px">RICE DISHES</div>
<div class="tab" style="left:889px;top:1619px;width:169px">ROAST &amp; GRILLS</div>
<div class="tab" style="left:169px;top:1680px;width:152px">FROM THE WOK</div>
<div class="tab" style="left:329px;top:1680px;width:144px">VEGETARIAN</div>
<div class="tab" style="left:482px;top:1680px;width:101px">SOUPS</div>
<div class="tab" style="left:592px;top:1680px;width:109px">EXTRAS</div>
<div class="tab" style="left:709px;top:1680px;width:169px">COLD BEVERAGES</div>
<div class="tab" style="left:887px;top:1680px;width:144px">POTS OF TEA</div>

<span class="arrow" style="left:37px"><svg width="36" height="36"><path d="M20,12 L14,18 L20,24" fill="none" stroke="#000" stroke-width="2.5"/></svg></span>
<span class="arrow" style="left:1126px"><svg width="36" height="36"><path d="M16,12 L22,18 L16,24" fill="none" stroke="#000" stroke-width="2.5"/></svg></span>

<div class="dish" style="left:112px"><div class="photo" role="img" aria-label="Diced noodle stir fry" style="background:radial-gradient(circle,#b08a4a,#8a6a3a 55%,#4a4a4a)"></div><div class="card"><div class="name">DING DING</div><div class="price">SML $19.80, LRG $37</div></div></div>
<div class="dish" style="left:364px"><div class="photo" role="img" aria-label="Flat noodles with vegetables" style="background:radial-gradient(circle,#d9a860,#a8743a 55%,#5a5a5a)"></div><div class="card"><div class="name">BESIP LAGMAN</div><div class="price">SML $19.80, LRG $37</div></div></div>
<div class="dish" style="left:616px"><div class="photo" role="img" aria-label="Golden meat pie cut into slices" style="background:radial-gradient(circle,#e0a460,#c07a3a 60%,#4a3a30)"></div><div class="card"><div class="name">GOSHNAN</div><div class="price">$21.00</div></div></div>
<div class="dish" style="left:868px"><div class="photo" role="img" aria-label="Baked samsa pastries on a plate" style="background:radial-gradient(circle,#d8c0a0,#8a8a88 60%,#3f4446)"></div><div class="card"><div class="name">SAMSA</div><div class="price">$21.00</div></div></div>

<h2 class="abs section-title center-title" style="top:2184px">OUR GALLERY</h2>
<span class="underline" style="top:2240px"></span>
<div class="tile" role="img" aria-label="Plate of boiled dumplings" style="left:111px;top:2289px;width:249px;height:404px;background:linear-gradient(160deg,#b8202a 0%,#d8d2c8 40%,#cfc8bc 70%,#b31f28)"></div>
<div class="tile" role="img" aria-label="Grilled meat skewers" style="left:377px;top:2289px;width:214px;height:188px;background:linear-gradient(135deg,#7a2a22,#a84a30 50%,#6a2a26)"></div>
<div class="tile" role="img" aria-label="Roast ribs on lettuce" style="left:609px;top:2289px;width:214px;height:188px;background:radial-gradient(circle,#5a3a28,#7a8a50 55%,#a32028)"></div>
<div class="tile" role="img" aria-label="Bowl of clear vegetable soup" style="left:377px;top:2496px;width:446px;height:196px;background:radial-gradient(ellipse,#d8ccb0,#eeeeea 45%,#5a3a2a 85%)"></div>
<div class="tile" role="img" aria-label="Spicy tofu with spring onion" style="left:840px;top:2289px;width:248px;height:404px;background:linear-gradient(160deg,#f0e0d0,#e8902a 30%,#b84a18 70%,#e8a040)"></div>

<footer>
  <svg class="abs" style="left:0;top:2800px" width="1200" height="538" viewBox="0 0 1200 538">
    <path d="M0,250 C150,-20 800,-20 1200,130 L1200,538 L0,538 Z" fill="#a81c24"/>
    <path d="M0,400 C150,30 800,-40 1200,185 L1200,538 L0,538 Z" fill="#000"/>
  </svg>
  <div class="brand" style="left:520px;top:2950px;font-size:30px"><i style="width:22px;height:22px"></i>KORAM</div>

  <div class="footer-col" style="left:111px">
    <h4>QUICK LINKS</h4>
    <div class="link"><svg width="14" height="14"><circle cx="7" cy="7" r="7" fill="#a81c24"/><path d="M4,7 H10 M7,4 L10,7 L7,10" stroke="#000" stroke-width="1.6" fill="none"/></svg>Home</div>
    <div class="link"><svg width="14" height="14"><circle cx="7" cy="7" r="7" fill="#a81c24"/><path d="M4,7 H10 M7,4 L10,7 L7,10" stroke="#000" stroke-width="1.6" fill="none"/></svg>Menu</div>
    <div class="link"><svg width="14" height="14"><circle cx="7" cy="7" r="7" fill="#a81c24"/><path d="M4,7 H10 M7,4 L10,7 L7,10" stroke="#000" stroke-width="1.6" fill="none"/></svg>Our Story</div>
    <div class="link"><svg width="14" height="14"><circle cx="7" cy="7" r="7" fill="#a81c24"/><path d="M4,7 H10 M7,4 L10,7 L7,10" stroke="#000" stroke-width="1.6" fill="none"/></svg>Contact Us</div>
  </div>

  <div class="footer-col" style="left:280px;width:250px">
    <h4>CONTACT INFO</h4>
    <div class="info"><svg width="14" height="16"><path d="M7,1 A5,5 0 0 1 12,6 C12,10 7,15 7,15 C7,15 2,10 2,6 A5,5 0 0 1 7,1 Z" fill="#a81c24"/><circle cx="7" cy="6" r="2" fill="#000"/></svg><div><b>ADDRESS:</b><span>Koram Noodle Bar 42 Harbour Lane<br>Milford 2190 NSW</span></div></div>
    <div class="info"><svg width="14" height="16"><path d="M3,2 L6,2 L7,5 L5,7 C6,9 7,10 9,11 L11,9 L14,10 L14,13 C8,14 2,8 3,2 Z" fill="#a81c24"/></svg><div><b>PHONE:</b><span>(02) 5550 1842</span></div></div>
    <div class="info"><svg width="14" height="16"><rect x="1" y="4" width="13" height="9" fill="#a81c24"/><path d="M1,4 L7.5,9 L14,4" stroke="#000" stroke-width="1.3" fill="none"/></svg><div><b>EMAIL:</b><span>hello@koramnoodles.com</span></div></div>
  </div>

  <div class="footer-col" style="left:548px;width:210px">
    <h4>TRADING HOURS</h4>
    <div class="info"><svg width="14" height="16"><circle cx="7" cy="8" r="6" fill="none" stroke="#a81c24" stroke-width="1.6"/><path d="M7,5 V8 H9.5" stroke="#a81c24" stroke-width="1.6" fill="none"/></svg><div><b>MONDAY TO SUNDAY:</b><span>11:30 am - 9:00 pm</span></div></div>
    <div class="info"><svg width="14" height="16"><circle cx="7" cy="8" r="6" fill="none" stroke="#a81c24" stroke-width="1.6"/><path d="M7,5 V8 H9.5" stroke="#a81c24" stroke-width="1.6" fill="none"/></svg><div><b>TUESDAY:</b><span>CLOSED</span></div></div>
  </div>

  <div class="footer-col" style="left:779px">
    <h4>SIGN UP TO OUR NEWSLETTER</h4>
    <div class="newsletter">Email Address<svg width="16" height="16"><path d="M1,8 L15,1 L10,15 L8,9 Z" fill="none" stroke="#a81c24" stroke-width="1.5"/></svg></div>
    <div style="display:flex;gap:8px;margin-top:20px"><span class="social red" style="position:static"></span><span class="social" style="position:static"></span><span class="social" style="position:static"></span></div>
  </div>

  <div class="abs rule"></div>
  <p class="abs copy">© 2024 KORAM &nbsp;|&nbsp; All Rights Reserved</p>
</footer>

</div>
</body>
</html>
```